Flier redesign

Sample fliers are attached from previous 2 years "Seasonal care 2018" and "2019 Seasonal Care" . Need an updated design for this year.

Possible images are attached to this brief. If you use the before/after pictures - you should use both of them. Use images attached to this brief or any from our website that you may prefer.

Colors

Designer to choose colors to be used in the design.

Requirements
Must have
• Colors should match our website theme. www.hollowbrookgardens.org
• Should be a "new" design, not just copying one of the prior year designs with a different image.
• Must be created in photoshop and file must be provided at the end.
• Text should be the same as 2019 version.

```html
<!DOCTYPE html>
<html lang="en">
<head>
<meta charset="utf-8">
<title>2019 Landscaping Package Flier</title>
<link href="https://fonts.googleapis.com/css2?family=Oswald:wght@500;700&family=Roboto:wght@400;500&family=Roboto+Condensed:wght@700&display=swap" rel="stylesheet">
<style>
  :root {
    --stage: #4aa6de;
    --paper: #ffffff;
    --brand-red: #c91f2a;
    --maroon: #7c1f30;
    --maroon-ink: #7a1b2b;
    --price-yellow: #ffe600;
    --text-light: #ffffff;
    --ink: #111111;
    --burst-outer: #ffb300;
    --burst-inner: #ffe23a;
  }
  * { box-sizing: border-box; margin: 0; padding: 0; }
  html, body { width: 1200px; height: 900px; overflow: hidden; background: var(--stage); }
  .flier {
    position: absolute; left: 290px; top: 15px;
    width: 620px; height: 870px; overflow: hidden;
    background: var(--paper);
    font-family: "Roboto", Arial, sans-serif;
    color: var(--text-light);
    box-shadow: 0 14px 30px rgba(0,0,0,.25);
  }
  .cemetery-photo {
    position: absolute; left: 0; top: 40px; width: 620px; height: 520px;
    background:
      radial-gradient(ellipse at 70% 10%, #b9d68a 0%, transparent 45%),
      linear-gradient(180deg, #4f7a2e 0%, #6f9a3c 40%, #8cbc50 62%, #5f8f35 100%);
  }
  .shapes { position: absolute; inset: 0; width: 620px; height: 870px; }
  .brand {
    position: absolute; top: 42px; right: 44px;
    display: flex; align-items: center; gap: 10px;
    font-family: "Roboto", Arial, sans-serif; font-weight: 500;
    font-size: 24px; letter-spacing: .5px; text-transform: uppercase;
    color: var(--maroon-ink);
  }
  .brand-mark { width: 40px; height: 40px; border-radius: 50%; border: 2px solid var(--maroon-ink); }
  .phone {
    position: absolute; top: 94px; right: 50px;
    display: flex; align-items: center; gap: 6px;
    font-family: "Roboto Condensed", Arial, sans-serif; font-weight: 700;
    font-size: 18px; color: var(--ink);
  }
  .headline {
    position: absolute; left: 42px; top: 142px;
    font-family: "Oswald", Impact, sans-serif; font-weight: 700;
    line-height: .98; color: var(--text-light);
    text-shadow: 0 2px 4px rgba(0,0,0,.35);
  }
  .headline .year { font-size: 64px; }
  .headline .word { font-size: 58px; display: block; }
  .headline .indent { padding-left: 72px; }
  .burst { position: absolute; left: 27px; top: 342px; width: 120px; height: 120px; }
  .burst-label {
    position: absolute; left: 27px; top: 370px; width: 120px;
    text-align: center; font-family: "Oswald", Impact, sans-serif; font-weight: 700;
    font-size: 24px; line-height: 1; color: var(--ink);
  }
  .tab {
    position: absolute; text-align: center;
    font-family: "Oswald", Impact, sans-serif; font-weight: 500;
    font-size: 17px; line-height: 1.35; color: var(--text-light);
  }
  .tab-seasonal { left: 19px; top: 517px; width: 174px; }
  .tab-basic { left: 218px; top: 476px; width: 178px; }
  .tab-perpetual { left: 427px; top: 400px; width: 173px; }
  .plan { position: absolute; }
  .plan-intro { text-align: center; font-size: 12px; line-height: 1.35; }
  .features { list-style: none; font-size: 10.5px; line-height: 1.35; }
  .features li { position: relative; padding-left: 20px; margin-bottom: 10px; }
  .features li::before { content: "\2714"; position: absolute; left: 2px; top: 0; font-size: 12px; }
  .plan-seasonal { left: 14px; top: 570px; width: 180px; }
  .plan-basic { left: 212px; top: 550px; width: 184px; }
  .plan-perpetual { left: 420px; top: 479px; width: 190px; }
  .plan-seasonal .features { margin-top: 14px; }
  .plan-basic .features { margin-top: 20px; }
  .plan-perpetual .features { margin-top: 16px; }
  .price-block { position: absolute; text-align: center; font-family: "Oswald", Impact, sans-serif; }
  .term { font-size: 17px; font-weight: 500; line-height: 1.1; }
  .price { color: var(--price-yellow); font-weight: 700; font-size: 28px; line-height: 1.1; }
  .price-small { color: var(--price-yellow); font-weight: 700; font-size: 18px; line-height: 1; }
  .price-pair { display: flex; justify-content: center; gap: 16px; margin-top: 8px; }
  .price-pair > div + div { border-left: 1.5px solid var(--text-light); padding-left: 16px; }
  .price-pair .term { font-size: 13px; }
  .fine-print {
    position: absolute; text-align: center;
    font-family: "Roboto Condensed", Arial, sans-serif; font-weight: 700;
    font-size: 8.5px; line-height: 1.45;
  }
  .price-seasonal { left: 0; top: 696px; width: 196px; }
  .fine-seasonal { left: 0; top: 808px; width: 196px; }
  .price-basic { left: 196px; top: 738px; width: 210px; }
  .price-basic .term { font-size: 17px; margin-bottom: 6px; }
  .price-basic .price, .price-perpetual .price { font-size: 30px; }
  .fine-basic { left: 196px; top: 808px; width: 210px; }
  .price-perpetual { left: 403px; top: 773px; width: 210px; }
  .fine-perpetual { left: 403px; top: 808px; width: 210px; }
  .footer {
    position: absolute; left: 0; bottom: 0; width: 620px; height: 30px;
    background: var(--brand-red);
    text-align: center; font-size: 10px; letter-spacing: 2px; line-height: 30px;
  }
</style>
</head>
<body>
<main class="flier">
  <div class="cemetery-photo" role="img" aria-label="Photo of a tree-lined cemetery lawn with rows of headstones"></div>

  <svg class="shapes" viewBox="0 0 620 870" aria-hidden="true">
    <path d="M0,0 H620 V110 C450,150 200,40 0,22 Z" fill="var(--paper)"/>
    <path d="M0,22 C200,40 450,150 620,110 V128 C450,172 200,100 0,60 Z" fill="var(--brand-red)"/>
    <path d="M0,530 H185 L205,490 H400 L420,445 H620 V840 H0 Z" fill="var(--maroon)"/>
    <polygon points="40,498 193,498 173,559 19,559" fill="var(--brand-red)"/>
    <polygon points="238,474 396,474 376,533 218,533" fill="var(--brand-red)"/>
    <polygon points="447,398 600,398 580,457 427,457" fill="var(--brand-red)"/>
    <line x1="196" y1="570" x2="196" y2="832" stroke="var(--text-light)" stroke-width="1.2"/>
    <line x1="403" y1="530" x2="403" y2="832" stroke="var(--text-light)" stroke-width="1.2"/>
  </svg>

  <div class="brand"><span>Hollowbrook Gardens</span><span class="brand-mark"></span></div>
  <div class="phone">
    <svg width="14" height="16" viewBox="0 0 14 16" aria-hidden="true"><rect x="0" y="0" width="14" height="16" rx="3" fill="var(--ink)"/><path d="M4 3 q-2 5 3 10 l2 -2 -2 -2 -1 1 q-2 -2 -1 -5 l1 0 0 -2 z" fill="var(--paper)"/></svg>
    <span>(555) 014-7260</span>
  </div>

  <h1 class="headline">
    <span class="word year">2019</span>
    <span class="word">LANDSCAPING</span>
    <span class="word indent">PACKAGE</span>
  </h1>

  <svg class="burst" viewBox="-60 -60 120 120" aria-hidden="true">
    <defs>
      <radialGradient id="burstFill"><stop offset="0" stop-color="var(--burst-inner)"/><stop offset="1" stop-color="var(--burst-outer)"/></radialGradient>
    </defs>
    <polygon fill="url(#burstFill)" points="0,-58 7,-46 18,-55 21,-42 34,-47 32,-34 46,-35 39,-23 53,-19 42,-10 55,-2 42,6 52,15 39,19 46,31 32,32 35,45 22,41 20,55 9,45 0,56 -9,45 -20,55 -22,41 -35,45 -32,32 -46,31 -39,19 -52,15 -42,6 -55,-2 -42,-10 -53,-19 -39,-23 -46,-35 -32,-34 -34,-47 -21,-42 -18,-55 -7,-46"/>
  </svg>
  <div class="burst-label">MOST<br>POPULAR</div>

  <div class="tab tab-seasonal">SEASONAL CARE</div>
  <div class="tab tab-basic">BASIC CARE<br>ENDOWNMENT</div>
  <div class="tab tab-perpetual">PERPETUAL CARE<br>ENDOWNMENT</div>

  <section class="plan plan-seasonal">
    <p class="plan-intro">Seasonal Landscaping<br>grave care.</p>
    <ul class="features">
      <li>Weeding and trimming services on your gravesite approximately 7 weeks during the growing season mid-April through mid-October</li>
    </ul>
  </section>
  <div class="price-block price-seasonal">
    <div class="term">3 YEARS</div>
    <div class="price">$ 345</div>
    <div class="price-pair">
      <div><div class="term">2 YEARS</div><div class="price-small">$ 230</div></div>
      <div><div class="term">1 YEAR</div><div class="price-small">$ 115</div></div>
    </div>
  </div>
  <p class="fine-print fine-seasonal">Mid year payment locks in current rates<br>Valid through 10/31/19</p>

  <section class="plan plan-basic">
    <p class="plan-intro">Landscaping care forever<br>graves with no plantings</p>
    <ul class="features">
      <li>Weeding and trimming services on your gravesite 2 times per year mid-May and mid-September</li>
      <li>Monument Leveling</li>
      <li>Payment ensures grave care forever</li>
    </ul>
  </section>
  <div class="price-block price-basic">
    <div class="term">12 MONTHLY PAYMENT OF</div>
    <div class="price">$ 239</div>
  </div>
  <p class="fine-print fine-basic">Call for single payment discount<br>Valid through 10/31/19</p>

  <section class="plan plan-perpetual">
    <p class="plan-intro">Landscaping care forever<br>graves with&nbsp; plantings</p>
    <ul class="features">
      <li>Weeding and trimming services on your gravesite approximately every 7 weeks during the growing seson: mid-April through mid-October</li>
      <li>Monument Leveling and cleaning</li>
      <li>Payment ensures grave care forever</li>
      <li>Full bed of boxwoods shcrubs</li>
      <li>Replacement of schrubs</li>
      <li>Trust certificate</li>
    </ul>
  </section>
  <div class="price-block price-perpetual">
    <div class="price">$ 297</div>
  </div>
  <p class="fine-print fine-perpetual">Call for single payment discount<br>Valid through 10/31/19</p>

  <footer class="footer">www.hollowbrookgardens.org</footer>
</main>
</body>
</html>
```